Leading In-Home Tutoring Company Needs Web Banners

We need a suite of web banners for our re-marketing campaign. We are based in Melbourne and heading into the busiest time of the year with back to school and we would like to help guide parents to working with us via quality designed banners with the right CTAs. Banner specs as follows (W x H in pixels)
Medium Rectangle: 300 x 250
Vertical rectangle: 240 x 400
Banner: 468 x 60
Leaderboard: 728 x 90
Square: 250 x 250
Mobile leaderboard: 320 x 50
Updates

Hi designers I'm new to this and didn't realise that I had to upload all files at the beginning. I have images that can be used for this project. Just need to work out how to upload them. Added Sunday, January 22, 2017

Hi awesome designers... I've updated the brief now with new files :)

Target Market(s)

Mothers who value kids education. Our customer can be found having morning coffee with friends in her lycra as she prepares to go to the gym. Middle class, inner city and suburban Mums. Most likely on Chatterloom.

Industry/Entity Type

It Company

Font styles to use
Sans Serif

Colors
0692cd
fbed22
f47f39
ec1f27

Requirements
Must have
• Wording should include.
• What we do: 1:1, In-Home Tutoring
• Value proposition: The Best Tutor For Your Child
• Call to Action - Free Assessment > Find Out More
• Adjusted layout to suit the sizes. Use of image where possible to provide immediate graphic display of what we do
Nice to have
• Keep it simple, create an emotive connection. Kids matter to parents and they will pay for services if we can create banners that show we care and can help wtih their education.
Should not have
• Anything negative or use fear marketing

```html
<!DOCTYPE html>
<html lang="en">
<head>
<meta charset="utf-8">
<title>Learnwise Web Banner Suite</title>
<link href="https://fonts.googleapis.com/css2?family=PT+Sans+Narrow:wght@400;700&display=swap" rel="stylesheet">
<style>
  :root {
    --orange: #f7901e;
    --orange-light: #fbb04f;
    --blue: #1a8ad8;
    --blue-light: #3aa6ee;
    --blue-dark: #3d7fb8;
    --ink: #474747;
    --red: #e53a2c;
    --white: #ffffff;
    --bg-centre: #f4f4f4;
    --bg-edge: #cfcfcf;
    --photo-a: #8fa6c4;
    --photo-b: #d8dde6;
  }
  * { box-sizing: border-box; margin: 0; padding: 0; }
  html, body { width: 1200px; height: 1200px; overflow: hidden; }
  body {
    font-family: "PT Sans Narrow", "Arial Narrow", sans-serif;
    font-weight: 700;
    background: radial-gradient(ellipse at 50% 45%, var(--bg-centre) 0%, #e6e6e6 55%, var(--bg-edge) 100%);
    position: relative;
  }
  .banner { position: absolute; overflow: hidden; box-shadow: 2px 3px 6px rgba(0,0,0,.25); }
  .banner > svg.art { position: absolute; inset: 0; width: 100%; height: 100%; }
  .abs { position: absolute; white-space: nowrap; line-height: 1; }
  .photo { position: absolute; background: linear-gradient(135deg, var(--photo-b), var(--photo-a)); }

  .brand { display: flex; align-items: center; gap: .3em; color: var(--blue); font-weight: 700; }
  .brand-dot { width: .55em; height: .55em; border-radius: 50%; background: var(--orange); }

  .cta {
    position: absolute; display: flex; align-items: center; justify-content: center; gap: .35em;
    border-radius: 999px; color: var(--white);
    background: linear-gradient(var(--blue-light), var(--blue));
    box-shadow: 0 2px 3px rgba(0,0,0,.25); white-space: nowrap; letter-spacing: -.2px;
  }
  .cta-icon { width: 1.1em; height: 1.1em; flex: none; }
  .cta--light { background: linear-gradient(#ffffff, #e4e4e4); color: var(--ink); }

  /* Vertical rectangle */
  .vertical { left: 132px; top: 95px; width: 324px; height: 536px; }
  .vertical .kicker { left: 22px; top: 50px; font-size: 30px; font-weight: 400; color: var(--ink); letter-spacing: -.5px; }
  .vertical .service { left: 21px; top: 80px; font-size: 40px; color: var(--white); letter-spacing: -.6px; }
  .vertical .headline { left: 0; right: 0; top: 194px; text-align: center; font-size: 44px; color: var(--ink); }
  .vertical .headline-accent { left: 0; right: 0; top: 240px; text-align: center; font-size: 44px; color: var(--blue); }
  .vertical .inset { left: 50px; top: 304px; width: 226px; height: 124px; border: 2px solid var(--orange); }
  .vertical .cta { left: 36px; top: 449px; width: 257px; height: 35px; font-size: 19px; }

  /* Square */
  .square { left: 497px; top: 296px; width: 402px; height: 334px; }
  .square .brand { position: absolute; left: 30px; top: 70px; font-size: 30px; }
  .square .headline { left: 0; right: 0; top: 170px; text-align: center; font-size: 30px; color: var(--white); }
  .square .cta { left: 47px; top: 213px; width: 316px; height: 40px; font-size: 24px; }
  .square .service { left: 0; right: 0; top: 270px; text-align: center; font-size: 31px; font-weight: 400; color: var(--white); }

  /* Horizontal strips */
  .strip .divider { position: absolute; width: 1px; background: #c9c9c9; }
  .strip .kicker { color: var(--ink); font-weight: 400; }
  .strip .service { color: var(--blue); font-weight: 400; }
  .strip .headline { color: var(--white); text-align: center; }

  .mobile { left: 132px; top: 686px; width: 430px; height: 68px; }
  .mobile .brand { position: absolute; left: 20px; top: 40px; font-size: 11px; }
  .mobile .divider { left: 102px; top: 14px; height: 44px; }
  .mobile .kicker { left: 109px; top: 24px; font-size: 14px; }
  .mobile .service { left: 108px; top: 37px; font-size: 21px; letter-spacing: -.4px; }
  .mobile .headline { left: 190px; width: 166px; top: 17px; font-size: 13px; letter-spacing: -.4px; }
  .mobile .cta { left: 210px; top: 36px; width: 126px; height: 15px; font-size: 8px; }

  .leader-sm { left: 132px; top: 819px; width: 626px; height: 78px; }
  .leader-sm .brand { position: absolute; left: 19px; top: 37px; font-size: 19px; }
  .leader-sm .divider { left: 147px; top: 14px; height: 52px; }
  .leader-sm .kicker { left: 155px; top: 19px; font-size: 21px; letter-spacing: -.3px; }
  .leader-sm .service { left: 154px; top: 40px; font-size: 29px; color: var(--red); letter-spacing: -.8px; }
  .leader-sm .headline { left: 284px; width: 230px; top: 13px; font-size: 21px; letter-spacing: -.3px; }
  .leader-sm .cta { left: 303px; top: 43px; width: 184px; height: 24px; font-size: 13px; }

  .leader { left: 132px; top: 943px; width: 977px; height: 123px; }
  .leader .brand { position: absolute; left: 32px; top: 58px; font-size: 30px; }
  .leader .divider { left: 227px; top: 20px; height: 84px; }
  .leader .kicker { left: 242px; top: 30px; font-size: 33px; letter-spacing: -.4px; }
  .leader .service { left: 241px; top: 62px; font-size: 44px; letter-spacing: -1px; }
  .leader .headline { left: 430px; width: 360px; top: 22px; font-size: 33px; letter-spacing: -.3px; }
  .leader .cta { left: 478px; top: 65px; width: 256px; height: 36px; font-size: 20px; }
</style>
</head>
<body>

<svg width="0" height="0" style="position:absolute">
  <defs>
    <symbol id="icon-arrow" viewBox="0 0 20 20">
      <circle cx="10" cy="10" r="9" fill="#ffffff"/>
      <path d="M8 5.5 L12.5 10 L8 14.5" fill="none" stroke="#1a8ad8" stroke-width="2.8" stroke-linecap="round" stroke-linejoin="round"/>
    </symbol>
    <linearGradient id="grey-body" x1="0" y1="0" x2="0" y2="1">
      <stop offset="0" stop-color="#d8d8d8"/><stop offset=".5" stop-color="#ffffff"/><stop offset="1" stop-color="#dcdcdc"/>
    </linearGradient>
    <linearGradient id="orange-body" x1="0" y1="0" x2="0" y2="1">
      <stop offset="0" stop-color="#f58a1f"/><stop offset=".5" stop-color="#fba84a"/><stop offset="1" stop-color="#f58a1f"/>
    </linearGradient>
    <linearGradient id="white-left" x1="0" y1="0" x2="1" y2="0">
      <stop offset="0" stop-color="#e9e9e9"/><stop offset=".5" stop-color="#ffffff"/><stop offset="1" stop-color="#f2f2f2"/>
    </linearGradient>
  </defs>
</svg>

<!-- Vertical rectangle 240x400 -->
<section class="banner vertical">
  <svg class="art" viewBox="0 0 324 536" preserveAspectRatio="none">
    <rect width="324" height="536" fill="url(#grey-body)"/>
    <path d="M0 0 H324 V150 C250 160 200 150 140 160 C80 170 30 185 0 200 Z" fill="var(--orange)"/>
    <path d="M0 200 C40 175 90 165 150 158 C220 150 270 160 324 140 V168 C270 185 220 175 150 182 C90 188 40 200 0 212 Z" fill="var(--blue)"/>
    <rect y="513" width="324" height="23" fill="var(--orange)"/>
  </svg>
  <div class="photo" role="img" aria-label="Tutor and schoolboy working together at a desk in front of a bookshelf"
       style="left:184px;top:0;width:140px;height:135px;clip-path:polygon(12% 0,100% 0,100% 100%,0 100%);"></div>
  <div class="abs kicker">1:1 IN-HOME</div>
  <div class="abs service">TUTORING</div>
  <div class="abs headline">The Best Tutor</div>
  <div class="abs headline-accent">For Your Child</div>
  <div class="photo inset" role="img" aria-label="Smiling tutor helping a girl with her schoolwork"></div>
  <a class="cta">Free Assessment - Find Out More <svg class="cta-icon"><use href="#icon-arrow"/></svg></a>
</section>

<!-- Square 250x250 -->
<section class="banner square">
  <svg class="art" viewBox="0 0 402 334" preserveAspectRatio="none">
    <rect width="402" height="334" fill="url(#orange-body)"/>
    <path d="M0 0 H402 V120 C330 140 280 150 200 150 C120 150 60 145 0 150 Z" fill="url(#grey-body)"/>
    <path d="M0 150 C60 145 120 140 200 142 C280 144 340 135 402 108 V125 C340 150 280 160 200 158 C120 156 60 160 0 166 Z" fill="var(--blue-dark)"/>
    <rect y="318" width="402" height="16" fill="var(--blue-dark)"/>
  </svg>
  <div class="photo" role="img" aria-label="Tutor and girl smiling over a workbook in front of a bookshelf"
       style="left:230px;top:0;width:172px;height:135px;clip-path:polygon(12% 0,100% 0,100% 80%,0 100%);"></div>
  <svg style="position:absolute;left:0;top:0;width:402px;height:140px" viewBox="0 0 402 140">
    <path d="M253 0 L230 135" stroke="var(--blue-dark)" stroke-width="5"/>
  </svg>
  <div class="brand"><span>Learnwise</span><span class="brand-dot"></span></div>
  <div class="abs headline">The Best Tutor For Your Child</div>
  <a class="cta">Free Assessment - Find Out More <svg class="cta-icon"><use href="#icon-arrow"/></svg></a>
  <div class="abs service">1:1 IN-HOME TUTORING</div>
</section>

<!-- Mobile leaderboard 320x50 -->
<section class="banner strip mobile">
  <svg class="art" viewBox="0 0 430 68" preserveAspectRatio="none">
    <rect width="430" height="68" fill="url(#white-left)"/>
    <path d="M0 0 H30 C12 10 6 30 6 68 H0 Z" fill="var(--blue)"/>
    <path d="M176 0 H370 L340 68 H218 C200 50 192 20 176 0 Z" fill="url(#orange-body)"/>
    <path d="M176 0 C192 20 200 50 218 68" fill="none" stroke="var(--blue-dark)" stroke-width="3"/>
  </svg>
  <div class="photo" role="img" aria-label="Tutor and girl working at a desk"
       style="left:340px;top:0;width:90px;height:68px;clip-path:polygon(33% 0,100% 0,100% 100%,0 100%);"></div>
  <div class="brand"><span>Learnwise</span><span class="brand-dot"></span></div>
  <span class="divider"></span>
  <div class="abs kicker">1:1 IN-HOME</div>
  <div class="abs service">TUTORING</div>
  <div class="abs headline">The Best Tutor For Your Child</div>
  <a class="cta">Free Assessment - Find Out More <svg class="cta-icon"><use href="#icon-arrow"/></svg></a>
</section>

<!-- Banner 468x60 -->
<section class="banner strip leader-sm">
  <svg class="art" viewBox="0 0 626 78" preserveAspectRatio="none">
    <rect width="626" height="78" fill="url(#white-left)"/>
    <path d="M0 0 H40 C16 12 10 35 10 78 H0 Z" fill="var(--blue)"/>
    <path d="M252 0 H540 L498 78 H298 C278 55 268 20 252 0 Z" fill="url(#orange-body)"/>
    <path d="M252 0 C268 20 278 55 298 78" fill="none" stroke="var(--blue-dark)" stroke-width="3.5"/>
  </svg>
  <div class="photo" role="img" aria-label="Tutor and girl smiling over schoolwork"
       style="left:498px;top:0;width:128px;height:78px;clip-path:polygon(33% 0,100% 0,100% 100%,0 100%);"></div>
  <div class="brand"><span>Learnwise</span><span class="brand-dot"></span></div>
  <span class="divider"></span>
  <div class="abs kicker">1:1 IN-HOME</div>
  <div class="abs service">TUTORING</div>
  <div class="abs headline">The Best Tutor For Your Child</div>
  <a class="cta cta--light">Free Assessment - Find Out More</a>
</section>

<!-- Leaderboard 728x90 -->
<section class="banner strip leader">
  <svg class="art" viewBox="0 0 977 123" preserveAspectRatio="none">
    <rect width="977" height="123" fill="url(#white-left)"/>
    <path d="M0 0 H62 C24 18 16 55 16 123 H0 Z" fill="var(--blue)"/>
    <path d="M384 0 H830 L760 123 H462 C432 88 414 30 384 0 Z" fill="url(#orange-body)"/>
    <path d="M384 0 C414 30 432 88 462 123" fill="none" stroke="var(--blue-dark)" stroke-width="5"/>
  </svg>
  <div class="photo" role="img" aria-label="Tutor and girl working together at a desk in front of a bookshelf"
       style="left:760px;top:0;width:217px;height:123px;clip-path:polygon(32% 0,100% 0,100% 100%,0 100%);"></div>
  <div class="brand"><span>Learnwise</span><span class="brand-dot"></span></div>
  <span class="divider"></span>
  <div class="abs kicker">1:1 IN-HOME</div>
  <div class="abs service">TUTORING</div>
  <div class="abs headline">The Best Tutor For Your Child</div>
  <a class="cta">Free Assessment - Find Out More <svg class="cta-icon"><use href="#icon-arrow"/></svg></a>
</section>

</body>
</html>
```